MEDICAL CLINIC LETTERHEAD

Design is a letterhead for a non-profit medical center. The name of the clinic is VITORRANE Community Health Center. Although the full name must be included, the community health center part is more of a description and should be less visible - i attached an example of what I mean by that (ATTACHED IMAGE IS AN EXAMPLE OF FONT SIZES NOT A DESIGN IDEA). Please design something modern, cool looking and unique because I can always download free templates.
Phone, email, website and etc will be added later.

Industry/Entity Type

MEDICAL

```html
<!DOCTYPE html>
<html lang="en">
<head>
<meta charset="utf-8">
<title>VITORRANE Community Health Center Letterhead</title>
<link href="https://fonts.googleapis.com/css2?family=Lato:wght@400;700&family=Figtree:wght@400;500&family=Italianno&display=swap" rel="stylesheet">
<style>
  :root {
    --navy: #1b2747;
    --gold: #b39259;
    --ink: #3a3a3a;
    --contact-ink: #1c1c1c;
    --paper: #ffffff;
    --paper-edge: #efefef;
    --backdrop: #e4e4e4;
  }
  * { margin: 0; padding: 0; box-sizing: border-box; }
  html, body {
    width: 1153px; height: 1200px; overflow: hidden;
    background: var(--backdrop);
  }
  .letterhead {
    position: absolute; left: 162px; top: 20px;
    width: 829px; height: 1160px; overflow: hidden;
    background: radial-gradient(ellipse at 50% 32%, var(--paper) 0%, #fbfbfb 35%, var(--paper-edge) 100%);
    font-family: "Lato", sans-serif; color: var(--ink);
  }
  .brand-mark {
    position: absolute; left: 60px; top: 82px;
    display: flex; align-items: center; gap: 12px;
  }
  .brand-mark .dot {
    width: 26px; height: 26px; border-radius: 50%; background: var(--gold);
  }
  .brand-mark .name {
    font-family: "Lato", sans-serif; font-weight: 700;
    font-size: 38px; letter-spacing: 1px; color: var(--navy);
  }
  .contact {
    position: absolute; left: 566px; top: 48px; height: 93px;
    border-left: 1.5px solid var(--gold); padding-left: 13px;
    font-family: "Figtree", sans-serif; font-size: 14.5px; color: var(--contact-ink);
    font-style: normal;
  }
  .contact .org { line-height: 18px; margin-top: -1px; }
  .contact ul { list-style: none; margin-top: 6px; }
  .contact li { display: flex; align-items: center; gap: 9px; height: 19.5px; }
  .contact svg { width: 14px; height: 12px; fill: var(--gold); }
  .letter { position: absolute; left: 64px; width: 701px; font-size: 15.8px; }
  .date { top: 256px; }
  .recipient { top: 295px; line-height: 19px; }
  .company { top: 351px; line-height: 19px; }
  .salutation { top: 430px; font-size: 20px; font-weight: 700; color: #333; }
  .body { top: 474px; line-height: 17.8px; text-align: justify; }
  .body p { margin-bottom: 17px; }
  .closing { top: 796px; }
  .signature {
    top: 838px; font-family: "Italianno", cursive; font-size: 46px; color: #2a2a2a;
  }
  .footer-band {
    position: absolute; left: 0; bottom: 0; width: 829px; height: 159px;
    background: linear-gradient(to bottom,
      rgba(239,239,239,0) 0%,
      rgba(179,146,89,0.55) 30%,
      var(--gold) 40%,
      var(--navy) 62%,
      var(--navy) 100%);
  }
</style>
</head>
<body>
  <main class="letterhead">
    <div class="brand-mark">
      <span class="dot"></span>
      <span class="name">VITORRANE</span>
    </div>

    <address class="contact">
      <div class="org">VITORRANE Community<br>Health Center</div>
      <ul>
        <li><svg viewBox="0 0 14 12"><path d="M1 4c0-2 3-3 6-3s6 1 6 3v1h-3V3.6C9 3.3 8 3.2 7 3.2S5 3.3 4 3.6V5H1zM3 6h8l2 5H1z"/></svg>987-555-0142</li>
        <li><svg viewBox="0 0 14 12"><path d="M0 1h14v10H0zM1 2.2v.4l6 4 6-4v-.4zM1 4v6h12V4L7 8z"/></svg>info@example-mail.com</li>
        <li><svg viewBox="0 0 14 12"><circle cx="7" cy="6" r="5.8"/></svg>www.example-web.com</li>
      </ul>
    </address>

    <div class="letter date">Feb-03-2022</div>
    <div class="letter recipient">Mr, Owen Marsh<br>President</div>
    <div class="letter company">Brightfield Corporation<br>123 Street Name, Suite# 10<br>City, State, 120023</div>
    <div class="letter salutation">Dear Mr, Owen</div>
    <div class="letter body">
      <p>Lorem ipsum dolor sit amet, consectetur adipisicing elit, sed do eiusmod tempor incididunt ut labore et dolore magna aliqua. Ut enim ad minim veniam, quis nostrud exercitation ullamco laboris nisi ut aliquip ex ea commodo consequat. Duis aute irure dolor in reprehenderit in voluptate velit esse cillum dolore eu fugiat nulla pariatur.</p>
      <p>Lorem ipsum dolor sit amet, consectetur adipisicing elit, sed do eiusmod tempor incididunt ut labore et dolore magna aliqua. Ut enim ad minim veniam, quis nostrud exercitation ullamco laboris nisi ut aliquip ex ea commodo consequat. Duis aute irure dolor in reprehenderit in voluptate velit esse cillum dolore eu fugiat nulla pariatur.</p>
      <p>Lorem ipsum dolor sit amet, consectetur adipisicing elit, sed do eiusmod tempor incididunt ut labore et dolore magna aliqua. Ut enim ad minim veniam, quis nostrud exercitation ullamco laboris nisi ut aliquip ex ea commodo consequat.</p>
      <p>Excepteur sint occaecat cupidatat non proident, sunt in culpa qui officia deserunt mollit anim id est laborum. re et dolore magnam aliquam quaerat voluptatem.</p>
    </div>
    <div class="letter closing">Regards</div>
    <div class="letter signature">Daniel Harwick</div>

    <div class="footer-band" role="img" aria-label="Decorative footer band in gold and navy tones"></div>
  </main>
</body>
</html>
```